I need a website design for a unique tropical home in the Whitsundays. It is called the Koruvel Grove and would like an African Baobab tree as a logo. It is an eco retreat on the ocean/beach with a large award winning house. Is suited to special celebrations, boutique weddings, Executive retreats. Have many wonderful photographs to be added. Should allow for contact to arrange a booking and if possible have a pricing and bookings calendar. Can look at Velmarra.com.au as example.
Home page should have picture of house from air and description of the special uses as mentioned above. Can then go to next level for descriptions of rooms, features, attractions, rates, booking calendar and contact details.

```html
<!DOCTYPE html>
<html lang="en">
<head>
<meta charset="utf-8">
<title>Koruvel Grove – Eco Retreat on the Ocean</title>
<link href="https://fonts.googleapis.com/css2?family=Open+Sans:wght@300;400;600&family=Montserrat:wght@400;500&display=swap" rel="stylesheet">
<style>
:root{
  --green:#1b8a1b;
  --green-dark:#0e6410;
  --green-deep:#0b5a0d;
  --green-text:#1a7a12;
  --orange:#f7941d;
  --orange-dark:#e57d06;
  --grey:#666;
  --grey-light:#8a8a8a;
  --line:#e2e2e2;
  --strip:#f4f4f4;
}
*{margin:0;padding:0;box-sizing:border-box}
html,body{width:993px;height:1200px;overflow:hidden;background:#fff}
body{position:relative;font-family:"Open Sans",Arial,sans-serif;color:var(--grey)}
.abs{position:absolute}

/* header */
.brand{left:85px;top:14px;display:flex;align-items:center;gap:8px}
.brand-mark{width:58px;height:78px;background:var(--green);border-radius:2px}
.brand-name{font-family:"Open Sans",sans-serif;font-weight:400;color:var(--green-text);font-size:30px;line-height:32px}
.enquiry{right:96px;top:44px;text-align:right}
.enquiry-label{color:var(--green-text);font-size:15px}
.enquiry-phone{color:var(--orange);font-size:23px;line-height:26px}

/* navigation */
.nav{left:0;top:104px;width:993px;height:41px;background:linear-gradient(#24a024,var(--green-dark));display:flex;padding-left:137px}
.nav a{display:block;height:41px;line-height:41px;color:#fff;text-decoration:none;font-size:15px;text-align:center;border-right:1px solid rgba(0,0,0,.18)}
.nav a:last-child{border-right:0}
.nav a.active{background:var(--green-deep)}

/* hero */
.hero{left:0;top:145px;width:993px;height:378px;background:linear-gradient(#6f8454 0%,#7f8c64 45%,#c9c2a2 60%,#6eaab0 75%,#4f98a6 100%)}
.hero-title{left:0;top:270px;width:993px;text-align:center;color:#fff;font-family:"Montserrat",sans-serif;font-size:44px;font-weight:400;text-shadow:0 1px 3px rgba(0,0,0,.4)}
.hero-sub{left:0;top:325px;width:993px;text-align:center;color:#fff;font-family:"Montserrat",sans-serif;font-size:22px;text-shadow:0 1px 3px rgba(0,0,0,.4)}
.dots{left:467px;top:499px;display:flex;gap:4px}
.dots span{width:12px;height:12px;border-radius:50%;background:rgba(255,255,255,.85)}

/* intro strip */
.strip{left:0;top:523px;width:993px;height:171px;background:linear-gradient(#fff,var(--strip))}
.card-photo{width:110px;height:110px;border-radius:3px;box-shadow:0 1px 3px rgba(0,0,0,.3)}
.card-title{color:var(--green-text);font-size:19px;white-space:nowrap}
.card-text{font-size:10px;line-height:15px;color:var(--grey-light);width:150px}
.btn{width:94px;height:27px;line-height:27px;text-align:center;font-size:11px;color:#fff;background:linear-gradient(var(--orange),var(--orange-dark));border-radius:2px}

/* content */
.h-welcome{left:86px;top:728px;font-size:22px;font-weight:400;color:#555;white-space:nowrap}
.para{left:87px;width:525px;font-size:10px;line-height:16px;color:var(--grey)}
.h-section{font-size:21px;font-weight:400;color:var(--green-text);white-space:nowrap}
.features{left:86px;top:919px;width:230px;list-style:none}
.features li{height:23px;line-height:23px;font-size:11px;color:var(--grey);border-bottom:1px solid var(--line);padding-left:18px;position:relative;white-space:nowrap;overflow:visible}
.features li:last-child{border-bottom:0}
.features svg{position:absolute;left:0;top:7px}
.gallery{left:354px;top:917px;display:grid;grid-template-columns:repeat(3,81px);grid-auto-rows:66px;gap:8px 8px}
.divider{left:650px;top:730px;width:1px;height:328px;background:var(--line)}

/* calendar */
.h-calendar{left:678px;top:726px;font-size:21px;font-weight:400;color:var(--orange)}
.calendar{left:678px;top:760px;width:210px;border:1px solid #ddd}
.cal-head{height:27px;background:var(--green);color:#fff;display:flex;align-items:center;justify-content:space-between;padding:0 10px;font-size:13px;border-radius:2px 2px 0 0}
.calendar table{width:100%;border-collapse:collapse;font-size:12px;text-align:center}
.calendar th{background:var(--orange);color:#fff;font-weight:400;font-size:11px;height:24px}
.calendar td{height:23.5px;border:1px solid #e4e4e4;color:#333}
.calendar td.muted{color:#aaa}
.calendar td.today{background:#222;color:#fff}
.h-connect{left:677px;top:968px;font-size:18px;font-weight:400;color:#444}
.connect-text{left:678px;top:993px;width:215px;font-size:10px;line-height:15px;color:var(--grey-light)}
.social{left:678px;top:1031px;display:flex;gap:8px}
.social span{width:19px;height:19px;border-radius:2px}

/* footer */
.footer{left:0;top:1101px;width:993px;height:99px;background:linear-gradient(#15761a,var(--green-deep))}
.footer-links{left:86px;top:1122px;color:#fff;font-size:13px}
.footer-links span{margin:0 6px}
.copyright{left:86px;top:1151px;color:#cfe5cf;font-size:10px}
</style>
</head>
<body>

<header>
  <div class="abs brand">
    <div class="brand-mark"></div>
    <div class="brand-name">Koruvel<br>Grove</div>
  </div>
  <div class="abs enquiry">
    <div class="enquiry-label">Enquiry Call Us</div>
    <div class="enquiry-phone">555.014.2290</div>
  </div>
</header>

<nav class="abs nav">
  <a class="active" style="width:81px">HOME</a>
  <a style="width:97px">ROOMS</a>
  <a style="width:107px">FEATURES</a>
  <a style="width:137px">ATTRACTIONS</a>
  <a style="width:82px">RATES</a>
  <a style="width:108px">BOOKING</a>
  <a style="width:106px">CONTACT</a>
</nav>

<section>
  <div class="abs hero" role="img" aria-label="Aerial photograph of the retreat among bushland beside a turquoise bay"></div>
  <h1 class="abs hero-title">An Eco retreat on the Ocean</h1>
  <p class="abs hero-sub">Suited to special celebrations, boutique weddings, Executive retreats</p>
  <div class="abs dots"><span></span><span></span><span></span><span></span></div>
</section>

<section class="abs strip"></section>

<div class="abs card-photo" style="left:87px;top:551px;background:linear-gradient(#a58356,#e8dcc4)" role="img" aria-label="Photo of an open lounge and dining room"></div>
<div class="abs card-title" style="left:206px;top:549px">What Specials</div>
<div class="abs card-text" style="left:207px;top:577px">In iaculis facilisis massa Etiam eu urna Sed porta Suspendisse quam leo molestie sed</div>
<div class="abs btn" style="left:207px;top:631px">READ MORE</div>

<div class="abs card-photo" style="left:367px;top:550px;background:linear-gradient(#d9b78a,#6b5238)" role="img" aria-label="Photo of a hammock on a veranda facing the sea"></div>
<div class="abs card-title" style="left:486px;top:548px">Why Us?</div>
<div class="abs card-text" style="left:487px;top:576px">In iaculis facilisis massa Etiam eu urna Sed porta Suspendisse quam leo molestie sed</div>
<div class="abs btn" style="left:487px;top:631px">READ MORE</div>

<div class="abs card-photo" style="left:646px;top:551px;background:linear-gradient(#b58a56,#e9e2d6)" role="img" aria-label="Photo of a made bed in a guest room"></div>
<div class="abs card-title" style="left:765px;top:549px">Rooms &amp; Other</div>
<div class="abs card-text" style="left:766px;top:577px">In iaculis facilisis massa Etiam eu urna Sed porta Suspendisse quam leo molestie sed</div>
<div class="abs btn" style="left:766px;top:631px">READ MORE</div>

<main>
  <h2 class="abs h-welcome">Welcome to Koruvel Grove Mainpage</h2>
  <p class="abs para" style="top:764px">Mauris vel lacus vitae felis vestibulum volutpat. Etiam est nunc, venenatis in, tristique eu, imperdiet ac, nisl. Cum soc iis natoque penatibus et magnis dis parturient montes, nascetur ridiculus mus.</p>
  <p class="abs para" style="top:804px">Mauris vel lacus vitae felis vestibulum volutpat. Etiam est nunc, venenatis in, tristique eu, imperdiet ac, nisl. Cum sociis natoque penatibus et magnis dis parturient montes, nascetur ridiculus mus. In iaculis facilisis massa. Etiam eu urna. Sed porta. Suspendisse quam leo, molestie sed, luctus quis, feugiat in, pede.</p>

  <h3 class="abs h-section" style="left:86px;top:872px">Features &amp; Services</h3>
  <ul class="abs features">
    <li><svg width="12" height="10" viewBox="0 0 12 10"><path d="M1 5l3.5 3.5L11 1" fill="none" stroke="#aaa" stroke-width="2"/></svg>Etiam est nunc venenatis</li>
    <li><svg width="12" height="10" viewBox="0 0 12 10"><path d="M1 5l3.5 3.5L11 1" fill="none" stroke="#aaa" stroke-width="2"/></svg>Cum sociis natoque penatibus magnis</li>
    <li><svg width="12" height="10" viewBox="0 0 12 10"><path d="M1 5l3.5 3.5L11 1" fill="none" stroke="#aaa" stroke-width="2"/></svg>Dis parturient montes nascetur ridiculus mus.</li>
    <li><svg width="12" height="10" viewBox="0 0 12 10"><path d="M1 5l3.5 3.5L11 1" fill="none" stroke="#aaa" stroke-width="2"/></svg>In iaculis facilisis massa.</li>
    <li><svg width="12" height="10" viewBox="0 0 12 10"><path d="M1 5l3.5 3.5L11 1" fill="none" stroke="#aaa" stroke-width="2"/></svg>Etiam eu urna Sed porta</li>
    <li><svg width="12" height="10" viewBox="0 0 12 10"><path d="M1 5l3.5 3.5L11 1" fill="none" stroke="#aaa" stroke-width="2"/></svg>Suspendisse quam leo molestie sed</li>
  </ul>

  <h3 class="abs h-section" style="left:352px;top:872px">Photo Gallery</h3>
  <div class="abs gallery">
    <div style="background:linear-gradient(#4a8fd8,#2aa2c2)" role="img" aria-label="Photo of palms over a resort pool"></div>
    <div style="background:linear-gradient(#efe9df,#c9b79b)" role="img" aria-label="Photo of breakfast served in a bright room"></div>
    <div style="background:linear-gradient(#8a6a4a,#5a7040)" role="img" aria-label="Photo of an ornate doorway with plants"></div>
    <div style="background:linear-gradient(#f2b04a,#8a5a2a)" role="img" aria-label="Photo of a couple dining at sunset"></div>
    <div style="background:linear-gradient(#6fa2d8,#5a9a3a)" role="img" aria-label="Photo of a large tree on a lawn"></div>
    <div style="background:linear-gradient(#9aa4ad,#6a4a32)" role="img" aria-label="Photo of a lounge with a city view"></div>
  </div>
</main>

<div class="abs divider"></div>

<aside>
  <h3 class="abs h-calendar">Booking Calender</h3>
  <div class="abs calendar">
    <div class="cal-head">
      <svg width="6" height="8" viewBox="0 0 6 8"><path d="M5 0v8L0 4z" fill="#fff"/></svg>
      <span>MARCH 2014</span>
      <svg width="6" height="8" viewBox="0 0 6 8"><path d="M1 0v8l5-4z" fill="#fff"/></svg>
    </div>
    <table>
      <tr><th>Su</th><th>Mo</th><th>Tu</th><th>We</th><th>Th</th><th>Fr</th><th>Sa</th></tr>
      <tr><td class="muted">28</td><td class="muted">29</td><td class="muted">30</td><td class="muted">31</td><td>1</td><td>2</td><td>3</td></tr>
      <tr><td>4</td><td>5</td><td>6</td><td>7</td><td>8</td><td>9</td><td>10</td></tr>
      <tr><td>11</td><td>12</td><td>13</td><td>14</td><td>15</td><td>16</td><td>17</td></tr>
      <tr><td>18</td><td>19</td><td class="today">20</td><td>21</td><td>22</td><td>23</td><td>24</td></tr>
      <tr><td>25</td><td>26</td><td>27</td><td>28</td><td>29</td><td>30</td><td class="muted">1</td></tr>
      <tr><td class="muted">2</td><td class="muted">3</td><td class="muted">4</td><td class="muted">5</td><td class="muted">6</td><td class="muted">7</td><td class="muted">8</td></tr>
    </table>
  </div>

  <h3 class="abs h-connect">Get Connected With Us</h3>
  <p class="abs connect-text">Cum sociis natoque penatibus et magnis dis parturient montes nascetur</p>
  <div class="abs social">
    <span style="background:#3b5998"></span>
    <span style="background:#35b7e8"></span>
    <span style="background:#1a6fa8"></span>
    <span style="background:#f26a1b"></span>
  </div>
</aside>

<footer>
  <div class="abs footer"></div>
  <div class="abs footer-links">Home<span>|</span>Rooms<span>|</span>Features<span>|</span>Attractions<span>|</span>Rates<span>|</span>Booking<span>|</span>Contact</div>
  <div class="abs copyright">© 2014 Company Name.&nbsp; All right reserved.&nbsp; Term of Use</div>
</footer>

</body>
</html>
```